New Business Card & Logo Design Project for PR Agency

Halvery & Partners Tech Public Relations agency is looking for a new business card design. Please see our website at www.halvery-pr.example for a description of our services. The design does not necessarily have to match the website’s aesthetic as we are looking for something fresh and modern that reflects our business. We want to emphasize that our focus is on media & public relations, content creation, social media and SEO. We want the business card to convey our BtoB technology focus and should have a very clean look. You are welcome to draw from our current halvery & partners logo on the card or play with that design too. We also like the idea of utilizing blue and white, which are often used in technology-related designs and layouts.
Attached are jpegs of the current logo and current card design for your reference.
Target Market(s)
Our clients are Business-to-Business technology providers.We sell our services to the CEO/President/Marketing director of a technology providing company.
Industry/Entity Type
Business
Look and feel

```html
<!DOCTYPE html>
<html lang="en">
<head>
<meta charset="utf-8">
<title>Halvery &amp; Partners – Business Card</title>
<link rel="stylesheet" href="https://fonts.googleapis.com/css2?family=Roboto+Condensed:ital,wght@0,400;0,700;1,400;1,700&display=swap">
<style>
  :root {
    --ink: #111111;
    --accent-blue: #1f3fe0;
    --paper-light: #ffffff;
    --paper-edge: #d3d8da;
    --swoosh-black: #141414;
    --wave-light: #6fd2fc;
    --wave-mid: #2a6ae8;
    --wave-deep: #0b1fc6;
    --on-blue: #ffffff;
  }
  * { margin: 0; padding: 0; box-sizing: border-box; }
  html, body { width: 1200px; height: 720px; overflow: hidden; background: #ffffff; }
  .card {
    position: relative;
    width: 1200px;
    height: 720px;
    overflow: hidden;
    font-family: "Roboto Condensed", sans-serif;
    color: var(--ink);
    background: radial-gradient(ellipse 70% 75% at 45% 45%, var(--paper-light) 0%, #f1f3f4 45%, var(--paper-edge) 100%);
  }
  .card-wave { position: absolute; inset: 0; width: 1200px; height: 720px; }
  .brand-name {
    position: absolute;
    left: 51px;
    top: 58px;
    font-size: 58px;
    font-weight: 700;
    letter-spacing: 1px;
    color: #222222;
    line-height: 1;
  }
  .person { position: absolute; left: 130px; top: 244px; }
  .person-name {
    font-size: 64px;
    font-style: italic;
    font-weight: 400;
    letter-spacing: -1.5px;
    line-height: 1;
  }
  .person-title {
    margin-top: 8px;
    font-size: 44px;
    font-style: italic;
    color: var(--accent-blue);
    line-height: 1;
  }
  .info {
    position: absolute;
    left: 784px;
    top: 131px;
    height: 254px;
    padding-left: 27px;
    border-left: 3px solid var(--ink);
  }
  .services { list-style: none; }
  .services li {
    font-size: 35px;
    font-style: italic;
    letter-spacing: -0.5px;
    line-height: 43px;
  }
  .contact { margin-top: 14px; }
  .contact p {
    font-size: 25px;
    font-style: italic;
    line-height: 35px;
    letter-spacing: -0.3px;
    white-space: nowrap;
  }
  .contact .label { font-style: normal; font-weight: 700; }
  .address {
    position: absolute;
    right: 50px;
    top: 596px;
    text-align: right;
    color: var(--on-blue);
    font-size: 39px;
    font-style: italic;
    line-height: 47px;
    letter-spacing: -0.5px;
  }
</style>
</head>
<body>
<div class="card">
  <svg class="card-wave" viewBox="0 0 1200 720" aria-hidden="true">
    <defs>
      <linearGradient id="wave-fill" x1="1" y1="0" x2="0.6" y2="1">
        <stop offset="0" stop-color="var(--wave-light)"/>
        <stop offset="0.45" stop-color="var(--wave-mid)"/>
        <stop offset="1" stop-color="var(--wave-deep)"/>
      </linearGradient>
    </defs>
    <path class="swoosh" fill="var(--swoosh-black)"
      d="M0 611 C300 592 560 505 820 468 C1000 443 1120 430 1200 424 L1200 440 C1000 452 720 520 460 598 C300 642 150 660 0 660 Z"/>
    <path class="wave" fill="url(#wave-fill)"
      d="M0 656 C150 656 300 636 460 596 C720 522 1000 456 1200 438 L1200 720 L0 720 Z"/>
  </svg>

  <div class="brand-name">halvery &amp; partners</div>

  <div class="person">
    <h1 class="person-name">Daniel Reyes</h1>
    <p class="person-title">Partner</p>
  </div>

  <div class="info">
    <ul class="services">
      <li>Public Relations</li>
      <li>Content Creation</li>
      <li>Social Media &amp; SEO</li>
    </ul>
    <div class="contact">
      <p><span class="label">Phone:</span> 555-010-284</p>
      <p><span class="label">E-Mail:</span> dreyes@halvery-pr.example</p>
      <p><span class="label">URL:</span> www.halvery-pr.example</p>
    </div>
  </div>

  <address class="address">
    48 Linden Avenue, Suite 2<br>
    Brookfield, Vermont 05036
  </address>
</div>
</body>
</html>
```